New online business - used mobile phones - needs unique eye catching web design that sets it apart

The Handset Bazaar
We are a new business looking for a rapid response for our web site design. We don't want a normal website....... we need to be creative - most important PLEASE view the attached files uploaded 3 March to ensure you get us :)
.
The Handset Bazaar buys new and damaged mobile phones from the public. A simple process they complete to sell their mobile to us; we want our website to reflect this.
Our website needs to be modern, edgy and fun, not corporate and definitely not like any other mobile phone buying site in the world today!!
Our name was taken from a play on the share/stock market which we have tried to bring into the design ....... it hasn't worked with early designs submitted. Now taking a different approach. Refer to new attached files which should help you visualise our concept.

We like layout from Artisan Hive – plvendrake #7318290 design as this is very close to our layout vision.
The first page to tell the public what we do, how we do it, and then they click to accept the instant online quote. (page two they complete details about the mobiles model & condition they are selling, then page three complete their personal details).
Our background preference is dark, blackboard or dark with slight texture
a) We love white on black/dark background either typewriter font or look like hand drawn refer to attached files & quillandfennel.com.au site to see. Would Label font work???

b) Where the light blue colour is on #7318290 this needs to be like chromadex colour classic green, fern green or bright green, not fluorescent lime green or an insipid green.

c) The banner says The Handset Bazaar is open........... for buying mobiles for cash $$$ (we need people to know we BUY used/damaged phones)

d) We love colour either solid colour or looks like it has been coloured in on our dark background. Open to white or pastel background versions refer to attached coffee file.
We like Chromadex Orange 021,Haute Red,Dazzling Blue, Cyan Blue, Beetroot Purple, Island Green.
e) How it works – underneath this title put Our deal …………. It’s easy as…………..quote, post, get paid!!!
Quote – first circle hand drawn icon showing mobile phone & $ sign. Underneath it says .....Obtain Quote for Model & Condition
Post – second circle hand drawn icon show parcel. Underneath it says Free Post
Paid – third circle hand drawn icon showing large $ sign. Underneath it says Payment in Two Days
Plans - is swapped for wording- Get Market Quote with a large button which says GO or CLICK HERE (they click on the button & it takes them to the next page)
f) FAQ
Allow for six FAQ’s we will forward correct content to you for final design layout.

g) About Us
Please allow about a paragraph of text here, we will forward correct content to you for final design layout.
h) Contact Us
At the bottom where normal website have ………. home, contact details, blog, etc, please only put Email us & Call us, then social media icons for FB, Linked In and Twitter

I) LOGO We don’t have one yet, just put The Handset Bazaar at the top & it needs to be large sized font ................we are new and we need to push our name
If you are not clear on our vision ..........please email me and I will reply very quickly.
Thank you for taking the time to read & understand & get us:)

Target Market(s)

20-45 years any body with a spare smart phone that is lying around and they can get cash for. Target market could be slightly older to 50 but focus of 20-40's

Industry/Entity Type

Business

Number of Pages Required

3 page

Font styles to use
Other font styles liked:
• handwritten font or typewriter font

Requirements
Must have
• Read only attached files dated 4 March, tech error with other files, being removed.
• 1 Layout design of Artisan Hive – plvendrake #7318290
• 2 Hand drawn icons - refer to files
• 3 White font needs to look like hand written refer to quillandfennel.com.au or typewriter font - large size font
• 4 Main colours are Black or dark background, green with white text, preference is hand drawn font. The three circles for quote, post & pay with hand drawn icons can be any colour ...... Purple for quote, orange for post & green for paid
• 5 Big green button underneath 3 circles quote/post/pay - customers click on big button to get instant quote
Nice to have
• Coloured in hand drawings as per file
• Great Hand drawings coloured in
Should not have
• NO template designs so it look like you just put some text & a photo. Don't fill the page with mobile phones, one or two is ok, mobile phone pictures date so fast.
• Cartoons

```html
<!DOCTYPE html>
<html lang="en">
<head>
<meta charset="utf-8">
<title>The Handset Bazaar</title>
<link href="https://fonts.googleapis.com/css2?family=Kalam:wght@300;400;700&family=Gochi+Hand&family=Open+Sans:wght@400&display=swap" rel="stylesheet">
<style>
:root{
  --orange:#ff5a00;
  --ink:#222;
  --white:#fff;
  --dark:#3a3637;
  --dark-2:#2f2c2e;
  --muted:#8a8a8a;
  --board:#f1f1f1;
  --hand:'Kalam', cursive;
  --marker:'Gochi Hand', cursive;
  --plain:'Open Sans', sans-serif;
}
*{box-sizing:border-box;margin:0;padding:0}
html,body{width:888px;height:1200px;overflow:hidden;background:#fff}
.page{position:relative;width:888px;height:1200px;overflow:hidden;font-family:var(--hand);color:var(--ink)}
.abs{position:absolute}

/* hero */
.hero{left:0;top:0;width:888px;height:226px;
  background:linear-gradient(100deg,#1f4a57 0%,#3d5468 30%,#5a4a5c 55%,#6a4c55 75%,#4d4242 100%)}
.nav{left:0;top:11px;width:888px;height:22px}
.nav-item{position:absolute;top:0;height:21px;border:1.5px solid var(--ink);background:var(--white);
  border-radius:6px 3px 7px 4px;font-family:var(--hand);font-size:14px;line-height:19px;text-align:center;color:var(--ink)}
.nav-item.is-active{background:var(--orange);border-color:var(--orange);color:var(--white)}
.search{position:absolute;left:575px;top:0;width:97px;height:20px;border:1.5px solid var(--white);border-radius:10px;
  color:var(--white);font-size:9px;line-height:17px;padding-left:8px}
.search svg{position:absolute;right:10px;top:3px}
.brand{left:205px;top:62px;width:260px;height:140px;display:flex;align-items:center;justify-content:center;text-align:center;
  font-family:var(--marker);font-size:44px;line-height:46px;color:var(--white)}
.tagline{left:480px;top:62px;width:230px;font-size:23px;line-height:31px;color:var(--white);font-weight:400}
.tag-arrow{left:462px;top:148px}
.cta-enter{left:528px;top:173px;width:100px;height:20px;background:rgba(120,120,120,.45);
  font-family:var(--marker);font-size:15px;line-height:20px;color:var(--orange);text-align:center}

/* what we do */
.services{left:0;top:226px;width:888px;height:234px;background:linear-gradient(90deg,#333033,#3c3738 50%,#3a3333)}
.section-title{position:absolute;left:0;width:888px;text-align:center;font-size:22px;line-height:26px}
.services .section-title{top:23px;color:var(--white)}
.service{position:absolute;top:66px;width:140px;text-align:center}
.service svg{display:block;margin:0 auto}
.service-label{font-family:var(--marker);font-size:15px;line-height:16px;color:var(--white);margin-top:6px}

/* quote form */
.quote{left:0;top:460px;width:888px;height:181px;background:var(--white)}
.quote .section-title{top:12px;color:var(--ink)}
.board{left:233px;top:37px;width:420px;height:116px;background:var(--board);border:1.5px solid #333;border-radius:12px 8px 14px 10px}
.field{position:absolute;height:25px;border:1.5px solid #333;border-radius:12px;background:var(--white);font-size:11.5px;line-height:22px;padding-left:12px}
.btn-go{position:absolute;left:280px;top:78px;width:100px;height:26px;border:2px solid #333;border-radius:13px;background:var(--orange);
  color:var(--white);font-size:12px;line-height:22px;text-align:center}

/* faq */
.faq{left:0;top:641px;width:888px;height:291px;background:var(--white);border-top:1px solid #ddd}
.faq .section-title{top:17px}
.faq-item{position:absolute;width:240px;height:80px}
.faq-avatar{position:absolute;left:0;top:1px;width:48px;height:48px;border:2px solid var(--orange);border-radius:6px;background:#f6eee8}
.faq-q{position:absolute;left:59px;top:-2px;font-family:var(--marker);font-size:13px;color:var(--ink)}
.faq-a{position:absolute;left:59px;top:15px;width:160px;font-size:9px;line-height:13.4px;color:var(--muted)}
.view-all{left:404px;top:249px;width:80px;height:22px;background:#d8d8d8;font-family:var(--marker);font-size:14px;line-height:22px;text-align:center}

/* about */
.about{left:0;top:932px;width:888px;height:145px;background:linear-gradient(90deg,#353235,#3d3738 60%,#3a3231)}
.about .section-title{top:14px;color:var(--white)}
.about-text{position:absolute;left:228px;top:54px;width:432px;font-size:9.5px;line-height:13.3px;color:#e6e6e6;text-align:center}
.read-more{left:404px;top:108px;width:80px;height:22px;background:rgba(110,110,110,.6);font-family:var(--marker);font-size:14px;line-height:22px;color:var(--white);text-align:center}

/* footer */
.footer{left:0;top:1077px;width:888px;height:107px;
  background:linear-gradient(90deg,#8fa37a 0%,#c98ca8 25%,#b497c6 45%,#d9a2a6 70%,#e89566 100%)}
.footer-title{position:absolute;top:11px;font-family:var(--marker);font-size:18px;color:var(--ink)}
.contact-line{position:absolute;left:240px;font-size:9.5px;color:#333;display:flex;align-items:center;gap:8px}
.map{left:364px;top:19px;width:179px;height:68px;border:2px solid #555;background:linear-gradient(135deg,#e8e2cf,#f1ecdc 50%,#d9e3c6)}
.social{position:absolute;top:50px;width:28px;height:28px;border:1.5px solid #444;border-radius:50%}
.bottom-bar{left:0;top:1184px;width:888px;height:16px;background:var(--orange);font-family:var(--plain);font-size:7.5px;line-height:16px;color:var(--white)}
</style>
</head>
<body>
<div class="page">

  <header class="hero abs">
    <nav class="nav abs">
      <span class="nav-item is-active" style="left:216px;width:55px">Home</span>
      <span class="nav-item" style="left:285px;width:91px">What We Do</span>
      <span class="nav-item" style="left:388px;width:84px">How We Do</span>
      <span class="nav-item" style="left:493px;width:57px">Contact</span>
      <span class="search">Search
        <svg width="12" height="12" viewBox="0 0 12 12"><circle cx="5" cy="5" r="3.5" fill="none" stroke="#fff" stroke-width="1.5"/><line x1="7.6" y1="7.6" x2="11" y2="11" stroke="#fff" stroke-width="1.5"/></svg>
      </span>
    </nav>
    <div class="brand abs">The Handset Bazaar</div>
    <p class="tagline abs">The Handset Bazaar is open for buying mobiles for cash</p>
    <svg class="tag-arrow abs" width="46" height="20" viewBox="0 0 46 20"><path d="M2 4 C8 14 26 16 42 14" fill="none" stroke="#fff" stroke-width="1.3"/><path d="M37 10 L43 14 L37 17" fill="none" stroke="#fff" stroke-width="1.3"/></svg>
    <div class="cta-enter abs">Enter Our Site</div>
  </header>

  <section class="services abs">
    <h2 class="section-title">What We Do...?</h2>
    <div class="service" style="left:226px">
      <svg width="110" height="110" viewBox="0 0 110 110">
        <circle cx="55" cy="55" r="51" fill="#343133" stroke="#cfcfcf" stroke-width="2"/>
        <rect x="38" y="28" width="32" height="52" rx="6" fill="none" stroke="#fff" stroke-width="3"/>
        <rect x="44" y="35" width="20" height="34" rx="2" fill="none" stroke="#fff" stroke-width="2.5"/>
        <circle cx="54" cy="74" r="2" fill="#fff"/>
      </svg>
      <p class="service-label">quote for model &amp; condition</p>
    </div>
    <div class="service" style="left:378px">
      <svg width="110" height="110" viewBox="0 0 110 110">
        <circle cx="55" cy="55" r="51" fill="#343133" stroke="#cfcfcf" stroke-width="2"/>
        <path d="M30 36 L80 36 L80 48 L30 48 Z" fill="none" stroke="#fff" stroke-width="3"/>
        <path d="M34 48 L34 80 L76 80 L76 48" fill="none" stroke="#fff" stroke-width="3"/>
        <rect x="46" y="56" width="18" height="8" fill="none" stroke="#fff" stroke-width="2.5"/>
      </svg>
      <p class="service-label">Free post</p>
    </div>
    <div class="service" style="left:528px">
      <svg width="110" height="110" viewBox="0 0 110 110">
        <circle cx="55" cy="55" r="51" fill="#343133" stroke="#cfcfcf" stroke-width="2"/>
        <text x="55" y="78" text-anchor="middle" font-family="Gochi Hand, cursive" font-size="62" fill="none" stroke="#fff" stroke-width="2.5">$</text>
      </svg>
      <p class="service-label">Free post</p>
    </div>
  </section>

  <section class="quote abs">
    <svg class="abs" style="left:0;top:0" width="888" height="60" viewBox="0 0 888 60">
      <path d="M260 0 C252 20 250 40 256 54" fill="none" stroke="#222" stroke-width="1.6"/>
      <path d="M628 0 C634 20 636 40 631 54" fill="none" stroke="#222" stroke-width="1.6"/>
    </svg>
    <h2 class="section-title">Get Market Quote</h2>
    <div class="board abs">
      <svg class="abs" style="left:0;top:0" width="420" height="116" viewBox="0 0 420 116">
        <circle cx="23" cy="17" r="3.5" fill="#222"/><circle cx="397" cy="17" r="3.5" fill="#222"/>
        <path d="M208 90 C230 86 250 82 262 80" fill="none" stroke="#ff5a00" stroke-width="2"/>
        <path d="M255 76 L263 80 L256 85" fill="none" stroke="#ff5a00" stroke-width="2"/>
      </svg>
      <span class="field" style="left:24px;top:30px;width:160px">Full Name</span>
      <span class="field" style="left:218px;top:28px;width:162px">Email Address</span>
      <span class="field" style="left:24px;top:76px;width:160px">Mobile Number</span>
      <span class="btn-go">Click Here</span>
    </div>
  </section>

  <section class="faq abs">
    <h2 class="section-title">Clients FAQ's</h2>
    <div class="faq-item" style="left:218px;top:60px"><span class="faq-avatar" role="img" aria-label="Hand-drawn client avatar"></span><h3 class="faq-q">The standard Lorem Ipsum</h3><p class="faq-a">Lorem Ipsum is simply dummy text of the printing and typesetting industry. Lorem Ipsum has been the industry's standard dummy text ever since the</p></div>
    <div class="faq-item" style="left:463px;top:60px"><span class="faq-avatar" role="img" aria-label="Hand-drawn client avatar"></span><h3 class="faq-q">The standard Lorem Ipsum</h3><p class="faq-a">Lorem Ipsum is simply dummy text of the printing and typesetting industry. Lorem Ipsum has been the industry's standard dummy text ever since the</p></div>
    <div class="faq-item" style="left:218px;top:150px"><span class="faq-avatar" role="img" aria-label="Hand-drawn client avatar"></span><h3 class="faq-q">The standard Lorem Ipsum</h3><p class="faq-a">Lorem Ipsum is simply dummy text of the printing and typesetting industry. Lorem Ipsum has been the industry's standard dummy text ever since the</p></div>
    <div class="faq-item" style="left:463px;top:150px"><span class="faq-avatar" role="img" aria-label="Hand-drawn client avatar"></span><h3 class="faq-q">The standard Lorem Ipsum</h3><p class="faq-a">Lorem Ipsum is simply dummy text of the printing and typesetting industry. Lorem Ipsum has been the industry's standard dummy text ever since the</p></div>
    <div class="view-all abs">View All</div>
  </section>

  <section class="about abs">
    <h2 class="section-title">About Us</h2>
    <p class="about-text">Lorem Ipsum is simply dummy text of the printing and typesetting industry. Lorem Ipsum has been the industry's standard dummy text ever since the 1500s, when an unknown printer took a galley of type and scrambled it to make a type specimen book. It has survived not only five centuries, but also the leap into electronic</p>
    <div class="read-more abs">Read More</div>
  </section>

  <footer class="footer abs">
    <h3 class="footer-title" style="left:240px">Contact Us</h3>
    <p class="contact-line" style="top:42px"><svg width="8" height="10" viewBox="0 0 8 10"><path d="M4 10 L1 5 A3 3 0 1 1 7 5 Z" fill="#555"/></svg>Lorem Ipsum is simply</p>
    <p class="contact-line" style="top:61px"><svg width="9" height="9" viewBox="0 0 9 9"><path d="M1 1 L3 1 L4 3 L3 4 Q4 6 5 6 L6 5 L8 6 L8 8 Q2 8 1 1 Z" fill="#555"/></svg>(987) 555-0142</p>
    <p class="contact-line" style="top:80px"><svg width="9" height="7" viewBox="0 0 9 7"><rect x="0.5" y="0.5" width="8" height="6" fill="none" stroke="#555"/><path d="M0.5 0.5 L4.5 4 L8.5 0.5" fill="none" stroke="#555"/></svg>www.handsetbazaar.com</p>
    <div class="map abs" role="img" aria-label="Street map showing the shop location"></div>
    <h3 class="footer-title" style="left:570px">Follow Us</h3>
    <span class="social" style="left:566px" role="img" aria-label="Social profile"></span>
    <span class="social" style="left:599px" role="img" aria-label="Social profile"></span>
    <span class="social" style="left:632px" role="img" aria-label="Social profile"></span>
  </footer>

  <div class="bottom-bar abs">
    <span class="abs" style="left:222px">All rights reserved© www.handsetbazaar.com</span>
    <span class="abs" style="left:558px">Terms &amp; Conditions</span>
    <span class="abs" style="left:631px;top:3px;width:1px;height:10px;background:#fff"></span>
    <span class="abs" style="left:640px">Sitemap</span>
  </div>

</div>
</body>
</html>
```